Very Simple/Minimal Business Card Design Project

The company operates in the industrial maritime infrastructure sector in Brazil. You can find more information on our website www.navortek.com.br WE NEED TO LOOK POWERFUL AND SERIOUS
I have attached a copy of the old cards. We would like something more professional / industrial / sexy that also includes the position.

The card can be double sided or not. We would like you to propose as many options.

Thank you
Updates

Many thanks, do let me know if you have any questions. I am under a lot of time pressure to try and have them printed over the next days or so.

Please could you use the following information

for the address: Rua Tapiraçu, 417 - Centro, Rio de Janeiro, 20034-118, Brasil

for the mobile: +55 21 8237 9412
for the landline: +55 21 4096 3578

and position:  Diretor Geral

Thakn you

Target Market(s)

Shipowners, bankers, industrial companies

Industry/Entity Type

Industrial

Requirements
Must have
• POWERFUL
SERIOUS
SOLID
BIG CORPORATION

```html
<!DOCTYPE html>
<html lang="pt-BR">
<head>
<meta charset="utf-8">
<title>Navortek – Business Card</title>
<link rel="stylesheet" href="https://fonts.googleapis.com/css2?family=Arimo:wght@400;700&display=swap">
<style>
  :root {
    --backdrop: #2b2b2d;
    --card-white: #ffffff;
    --brand-green: #0b9a48;
    --brand-navy: #1f2a6e;
    --text-grey: #4a4f5c;
    --soft-grey: #eef0f2;
  }
  * { box-sizing: border-box; margin: 0; padding: 0; }
  html, body {
    width: 1200px; height: 900px; overflow: hidden;
    background: var(--backdrop);
    font-family: "Arimo", Arial, sans-serif;
  }
  .stage {
    position: relative; width: 1200px; height: 900px;
    display: flex; align-items: center; justify-content: center; gap: 40px;
  }
  .card {
    position: relative; width: 540px; height: 310px;
    box-shadow: 0 10px 28px rgba(0,0,0,.45);
  }

  /* Front side */
  .card--front { background: linear-gradient(135deg, var(--card-white) 60%, var(--soft-grey)); }
  .wordmark { display: flex; align-items: center; gap: 12px; }
  .wordmark__square { width: 34px; height: 34px; background: var(--brand-green); border-radius: 4px; }
  .wordmark__name { font-weight: 700; letter-spacing: .5px; }
  .card--front .wordmark { position: absolute; left: 40px; top: 58px; }
  .card--front .wordmark__name { font-size: 38px; color: var(--brand-navy); }

  .holder { position: absolute; left: 40px; top: 128px; }
  .holder__name { font-size: 20px; font-weight: 700; color: var(--brand-green); }
  .holder__role { font-size: 13px; color: var(--text-grey); margin-top: 2px; }

  .contacts { position: absolute; left: 40px; top: 188px; list-style: none; }
  .contacts li {
    display: flex; align-items: center; gap: 8px;
    font-size: 13px; color: var(--brand-navy); line-height: 21px;
  }
  .contacts svg { width: 13px; height: 13px; fill: var(--brand-green); flex: none; }

  .address {
    position: absolute; left: 330px; top: 132px;
    font-size: 13px; line-height: 19px; color: var(--brand-navy); font-style: normal;
  }

  /* Back side */
  .card--back {
    background: var(--brand-green);
    display: flex; flex-direction: column; align-items: center; justify-content: center; gap: 18px;
  }
  .card--back .wordmark { flex-direction: column; gap: 14px; }
  .card--back .wordmark__square { width: 62px; height: 52px; background: var(--card-white); border-radius: 6px; }
  .card--back .wordmark__name { font-size: 54px; color: var(--card-white); letter-spacing: 1px; }
  .web { font-size: 17px; font-weight: 700; color: var(--card-white); }
</style>
</head>
<body>
<main class="stage">

  <section class="card card--front" aria-label="Front of business card">
    <div class="wordmark">
      <span class="wordmark__square"></span>
      <span class="wordmark__name">NAVORTEK</span>
    </div>

    <div class="holder">
      <p class="holder__name">RAFAEL MOREIRA</p>
      <p class="holder__role">Diretor Geral</p>
    </div>

    <ul class="contacts">
      <li>
        <svg viewBox="0 0 24 24"><path d="M6.6 10.8a15.1 15.1 0 0 0 6.6 6.6l2.2-2.2a1 1 0 0 1 1-.25 11.4 11.4 0 0 0 3.6.57 1 1 0 0 1 1 1V20a1 1 0 0 1-1 1A17 17 0 0 1 3 4a1 1 0 0 1 1-1h3.5a1 1 0 0 1 1 1c0 1.25.2 2.45.57 3.57a1 1 0 0 1-.25 1z"/></svg>
        +55 21 4096 3578
      </li>
      <li>
        <svg viewBox="0 0 24 24"><path d="M7 1h10a2 2 0 0 1 2 2v18a2 2 0 0 1-2 2H7a2 2 0 0 1-2-2V3a2 2 0 0 1 2-2zm0 3v14h10V4zm5 15.5a1.2 1.2 0 1 0 0 2.4 1.2 1.2 0 0 0 0-2.4z"/></svg>
        +55 21 8237 9412
      </li>
      <li>
        <svg viewBox="0 0 24 24"><path d="M2 4h20v16H2zm2 2v.4l8 5.3 8-5.3V6zm0 2.8V18h16V8.8l-8 5.3z"/></svg>
        rafael@navortek.com.br
      </li>
      <li>
        <svg viewBox="0 0 24 24"><path d="M12 2a10 10 0 1 0 0 20 10 10 0 0 0 0-20zm6.9 6h-3a15 15 0 0 0-1.3-3.9A8 8 0 0 1 18.9 8zM12 4c.8 1.2 1.5 2.5 1.9 4h-3.8c.4-1.5 1.1-2.8 1.9-4zM4.3 14a8 8 0 0 1 0-4h3.4a16 16 0 0 0 0 4zm.8 2h3a15 15 0 0 0 1.3 3.9A8 8 0 0 1 5.1 16zm3-8h-3a8 8 0 0 1 4.3-3.9A15 15 0 0 0 8.1 8zM12 20c-.8-1.2-1.5-2.5-1.9-4h3.8c-.4 1.5-1.1 2.8-1.9 4zm2.3-6H9.7a14 14 0 0 1 0-4h4.6a14 14 0 0 1 0 4zm.3 5.9a15 15 0 0 0 1.3-3.9h3a8 8 0 0 1-4.3 3.9zm1.7-5.9a16 16 0 0 0 0-4h3.4a8 8 0 0 1 0 4z"/></svg>
        www.navortek.com.br
      </li>
    </ul>

    <address class="address">
      Rua Tapiraçu, 417 - Centro<br>
      Rio de Janeiro<br>
      20034-118<br>
      Brasil
    </address>
  </section>

  <section class="card card--back" aria-label="Back of business card">
    <div class="wordmark">
      <span class="wordmark__square"></span>
      <span class="wordmark__name">NAVORTEK</span>
    </div>
    <p class="web">www.navortek.com.br</p>
  </section>

</main>
</body>
</html>
```